Business Card Design Project

I own a dental practice and would like to use a logo that was recently designed to make business cards.
I am looking for a clean card with the following information on the card.

Halvorsen Dental Center (Using the logo)
Martin L. Halvorsen, D.D.S.
7234 Pinewick Ave. Suite B
Colorado Springs, CO 80547
(719) 482-6130
halvorsendentalcenter@mailbox-example.net
www.halvorsendentalcenter.example

Also a list of items on the back:
Services include

Family Dentistry
Cosmetic
Whitening
Tooth Colored Fillings
Crowns/Bridges
Implants/Tooth Replacement
Dentures
Root Canals
Updates

Just an FYI, I added an email address and website address.

I also added my Pic.  Please give designs with and without the pic

Thanks

Target Market(s)

20-70 U.S. Female that handles the household budget.

Industry/Entity Type

Dental

Requirements
Must have
• The logo is key. The color scheme of the logo is also key. The back of the business card should have the list of Dental Services offered at the practice. The front should be clean and professional looking. No cartoons. I will also include a picture of myself. I think that the final card may or may not include this picture, so the card designs should come with and without the picture. USE THE BLUE LOGO ONLY!!!
Should not have
• NO teeth should be on the card.

```html
<!DOCTYPE html>
<html lang="en">
<head>
<meta charset="utf-8">
<title>Halvorsen Dental Center – Business Card</title>
<link href="https://fonts.googleapis.com/css2?family=Roboto:wght@300;400;700&display=swap" rel="stylesheet">
<style>
  :root {
    --page-bg: #e9e7e3;
    --card-bg: #f1f1f0;
    --brand-blue: #5a8596;
    --text-grey: #4e4d4b;
    --text-dark: #3a3633;
    --photo-dark: #33363d;
    --photo-light: #5d6068;
    --card-shadow: rgba(0,0,0,0.16);
  }
  * { box-sizing: border-box; margin: 0; padding: 0; }
  html, body {
    width: 1200px; height: 900px; overflow: hidden;
    background: var(--page-bg);
    font-family: "Roboto", Arial, sans-serif;
  }
  .sheet {
    width: 1200px; height: 900px;
    display: flex; flex-direction: column;
    align-items: center; justify-content: center; gap: 34px;
  }
  .card {
    position: relative;
    width: 700px; height: 400px;
    background: var(--card-bg);
    box-shadow: 0 4px 14px var(--card-shadow);
    overflow: hidden;
  }

  /* Back: services */
  .card-back {
    display: flex; flex-direction: column; align-items: center; justify-content: center;
    text-align: center;
  }
  .brand {
    display: flex; align-items: center; gap: 14px;
  }
  .brand-dot {
    width: 18px; height: 18px; border-radius: 50%;
    background: var(--brand-blue);
  }
  .brand-name {
    font-size: 34px; font-weight: 400; color: var(--brand-blue);
    letter-spacing: 0.5px;
  }
  .back-rule {
    width: 470px; height: 2px; background: var(--brand-blue);
    margin: 34px 0 30px;
  }
  .services {
    list-style: none;
    font-size: 21px; font-weight: 300; color: var(--text-grey);
    line-height: 1.3;
  }

  /* Front: contact */
  .photo {
    position: absolute; top: 0; right: 0;
    width: 320px; height: 376px;
    background: radial-gradient(ellipse at 55% 45%, var(--photo-light), var(--photo-dark) 75%);
  }
  .stripe {
    position: absolute; left: 0; right: 0; bottom: 0;
    height: 24px; background: var(--brand-blue);
  }
  .contact {
    position: absolute; left: 46px; top: 118px; width: 330px;
    color: var(--text-grey);
  }
  .contact-name {
    font-size: 25px; font-weight: 300; color: var(--text-dark);
    padding-bottom: 14px;
  }
  .contact-rule {
    width: 318px; height: 2px; background: var(--brand-blue);
    margin-bottom: 18px;
  }
  .contact-lines { font-size: 16px; font-weight: 300; line-height: 1.4; }
  .contact-line { display: flex; gap: 10px; }
  .contact-label { color: var(--brand-blue); width: 12px; font-weight: 400; }
  .contact-value { white-space: nowrap; font-size: 15px; }
  .address { margin-top: 20px; font-size: 17px; font-weight: 300; line-height: 1.4; }
  .website { margin-top: 22px; font-size: 17px; font-weight: 700; color: var(--text-dark); }
</style>
</head>
<body>
<main class="sheet">
  <section class="card card-back">
    <div class="brand">
      <span class="brand-dot"></span>
      <span class="brand-name">Halvorsen Dental Center</span>
    </div>
    <div class="back-rule"></div>
    <ul class="services">
      <li>Family Dentistry • Cosmetic • Whitening</li>
      <li>Tooth Colored Fillings • Crowns/Bridges</li>
      <li>Implants/Tooth Replacement</li>
      <li>Dentures • Root Canals</li>
    </ul>
  </section>

  <section class="card card-front">
    <div class="photo" role="img" aria-label="Portrait photo of Dr. Martin L. Halvorsen"></div>
    <div class="stripe"></div>
    <div class="contact">
      <p class="contact-name">Martin L. Halvorsen, D.D.S.</p>
      <div class="contact-rule"></div>
      <div class="contact-lines">
        <p class="contact-line"><span class="contact-label">T</span><span class="contact-value">(719) 482-6130</span></p>
        <p class="contact-line"><span class="contact-label">E</span><span class="contact-value">halvorsendentalcenter@mailbox-example.net</span></p>
      </div>
      <p class="address">7234 Pinewick Ave. Suite B<br>Colorado Springs, CO 80547</p>
      <p class="website">www.halvorsendentalcenter.example</p>
    </div>
  </section>
</main>
</body>
</html>
```